DJ Marcus Tevane

I'm looking for a professional but still artsy/progressive design. I come from a hip hop/club DJ background playing a lot of underground music but have switched to doing more corporate parties and weddings recently. I am all about keeping the dancefloor moving and emotionally connecting with the crowd. I'd like a trendy/updated color palette. Something that's clean enough that looks professional but also trendy enough to convey that by the end of the night we'll be sweatily dancing to the latest hits. Some designers/artists I like: Rolo Pemberack, Gavin Struthe, Dorian Fellick, Orbitex 3100, Wade Ipsley.

```html
<!DOCTYPE html>
<html lang="en">
<head>
<meta charset="utf-8">
<title>DJ Marcus Tevane – Business Card</title>
<link rel="stylesheet" href="https://fonts.googleapis.com/css2?family=Roboto+Slab:wght@400;700&display=swap">
<style>
  :root {
    --backdrop: #141414;
    --card: #1f1f1f;
    --card-sheen: #2a2a2a;
    --emboss: #161616;
    --emboss-edge: #333333;
    --gloss-dark: #2b2b2b;
    --gloss-light: #f2f2f2;
    --contact: #d6d6d6;
    --rule: #4a4a4a;
  }
  * { margin: 0; padding: 0; box-sizing: border-box; }
  html, body {
    width: 1200px; height: 900px; overflow: hidden;
    background: var(--backdrop);
    font-family: "Roboto Slab", Georgia, serif;
  }
  .canvas {
    width: 1200px; height: 900px;
    display: flex; flex-direction: column; align-items: center; justify-content: center;
    gap: 40px;
  }
  .card {
    width: 640px; height: 366px;
    background: linear-gradient(135deg, var(--card) 0%, var(--card) 55%, var(--card-sheen) 80%, var(--card) 100%);
    position: relative;
    display: flex; align-items: center;
  }
  .card-front { justify-content: center; }
  .front-name {
    font-weight: 700; font-size: 44px; letter-spacing: 1px; text-transform: uppercase;
    background: linear-gradient(90deg, var(--gloss-dark) 0%, #5a5a5a 40%, var(--gloss-light) 85%);
    -webkit-background-clip: text; background-clip: text; color: transparent;
  }
  .card-back { padding-left: 70px; gap: 28px; }
  .back-name {
    font-weight: 700; font-size: 27px; text-transform: uppercase; letter-spacing: 0.5px;
    color: var(--emboss);
    text-shadow: 1px 1px 0 var(--emboss-edge), -1px -1px 0 #0c0c0c;
    white-space: nowrap;
  }
  .divider { width: 1px; height: 72px; background: var(--rule); }
  .contact-list { list-style: none; color: var(--contact); font-size: 16px; line-height: 1.55; }
  .contact-label { display: inline-block; width: 30px; }
</style>
</head>
<body>
  <main class="canvas">
    <section class="card card-front">
      <h1 class="front-name">DJ Marcus Tevane</h1>
    </section>
    <section class="card card-back">
      <p class="back-name">DJ Marcus Tevane</p>
      <span class="divider"></span>
      <ul class="contact-list">
        <li><span class="contact-label">P :</span>+330 2471-5063</li>
        <li><span class="contact-label">E :</span>info@DJMarcusTevane.com</li>
        <li><span class="contact-label">W :</span>latenightgroove.com</li>
      </ul>
    </section>
  </main>
</body>
</html>
```